Toy Company Needs a Web Site For a New Toy

We need a web site for a new toy called "Zippa Roller". The bike is a plastic, non motorized ride on toy for kids ages 1.5 - 5 years of age. The bike is being launched in three colors, red, blue and pink, though we may include a black option too.

For the web site we want something bold and colorful that communicates fun, therefore NO dull colors like black or grey. Nothing too cluttered. We want the site to attract the attention of kids but also give the parents a sense of confidence in our professionalism as a trustworthy toy company. The home page should focus on the bike, with different views of the bike and a small write-up on some of its key features. We would also like the home page to have a video of the bike in play. A obvious link to the shopping basket must be present as well. The site must include a shopping basket and ordering system.

Attached is a screenshot of a site that has the colourfulness and playfulness that we are looking for. Please have a look.

The bike images attached are renderings from the CAD software, actual high res photos will be used when the site is developed.

The product logo is attached and MUST be used on the site. It must be BOLD and can be incorporated into the actual website design.

The site pages are:
Home
Gallery
Buy
Contact

Competitors:
www.brimvalekids.example
www.quorvaride.example
I do not like either of their sites.

We only have one product at this time, so the site is to be focused on that product, not a whole catalog of products. It is really a single product with the ability to purchase.
Updates

Project Deadline Extended
Reason: I am extending this competition in order to give me more time to review each design and provide the feedback that the designers deserve.

Target Market(s)

Parents, children ages 1.5 - 5.

Industry/Entity Type

It Company

Colors
0555a3
eb1f27
9bcb3c
faed22
f78f20
f37022
e34197
a6459a
6b449b

Requirements
Must have
• Please use the logo attached, but feel free to use different colors.
Should not have
• Dull colors like black and grey

```html
<!DOCTYPE html>
<html lang="en">
<head>
<meta charset="utf-8">
<title>Zippa Roller</title>
<link href="https://fonts.googleapis.com/css2?family=Arimo:wght@400;700&display=swap" rel="stylesheet">
<style>
:root{
  --backdrop:#1c1c1e;
  --page:#f3f3f3;
  --nav-top:#2478e0;
  --nav-bottom:#0f56bb;
  --nav-green:#6cb623;
  --pink:#e63e74;
  --pink-dark:#c72a5c;
  --navy:#0e4fb3;
  --label-blue:#1b6fd8;
  --footer:#1b74e2;
  --footer-bar:#0f5cc4;
  --text:#222;
  --white:#fff;
}
*{margin:0;padding:0;box-sizing:border-box}
html,body{width:812px;height:1200px;overflow:hidden}
body{background:var(--backdrop);font-family:"Arimo",Arial,sans-serif;color:var(--text);position:relative}
.page{position:absolute;left:78px;top:0;width:656px;height:1200px;background:var(--page)}
.abs{position:absolute}
.photo{position:absolute}

/* navigation */
.nav{left:73px;top:27px;width:665px;height:39px;background:linear-gradient(var(--nav-top),var(--nav-bottom));z-index:2}
.nav a{position:absolute;top:0;height:39px;line-height:39px;color:var(--white);font-size:9.5px;text-decoration:none}
.nav .home{left:31px;width:44px;text-align:center;background:var(--nav-green)}
.cart-link{left:495px;top:0;width:145px;height:39px;background:var(--nav-green);color:var(--white);font-size:7.5px;font-family:"Times New Roman",serif;line-height:39px;padding-left:32px}
.cart-link svg{position:absolute;left:8px;top:11px}
.logo{left:357px;top:0;width:112px;height:112px;border-radius:50%;background:var(--white);border:5px solid var(--label-blue);display:flex;align-items:center;justify-content:center;text-align:center;z-index:5;box-shadow:0 2px 4px rgba(0,0,0,.25)}
.logo span{font-size:16px;font-weight:700;color:var(--label-blue);line-height:1.15}

/* hero */
.hero{left:78px;top:66px;width:656px;height:250px;background:linear-gradient(90deg,#7b8a6c 0%,#5f8f3a 40%,#6aa336 70%,#8ab05a 100%)}
.caption{position:absolute;left:121px;background:var(--white);padding:0 7px;height:24px;line-height:24px;font-size:13px}
.cap1{top:122px;color:var(--label-blue)}
.cap2{top:151px;color:var(--nav-green)}
.cap3{top:180px;color:var(--label-blue)}
.hero-btn{left:121px;top:210px;width:62px;height:22px;background:var(--navy);color:var(--white);font-size:8px;line-height:22px;text-align:center;border-radius:2px}
.slider{left:331px;top:306px;width:149px;height:18px;border-radius:9px;background:linear-gradient(#f7f7f7,#d6d6d6);box-shadow:0 1px 2px rgba(0,0,0,.3)}
.slider i{position:absolute;top:7px;width:5px;height:5px;border-radius:50%;background:#aaa}
.slider i.on{background:var(--label-blue)}
.slider b{position:absolute;top:3px;font-size:9px;color:#888;font-weight:400}

/* product */
.panel{background:#fafafa;border:1px solid #ddd;box-shadow:0 1px 3px rgba(0,0,0,.1)}
.product{left:91px;top:352px;width:382px;height:242px}
.product-photo{left:102px;top:362px;width:360px;height:224px;background:linear-gradient(#4a6b3a,#707070 55%,#4d4d4d)}
.price-tag{left:484px;top:362px}
.price-tag .name{left:28px;top:15px;color:var(--white);font-size:14px;white-space:nowrap}
.price-tag .price{left:142px;top:15px;color:var(--white);font-size:14px;white-space:nowrap}
.label{color:var(--label-blue);font-size:13px}
.swatch{top:428px;width:15px;height:14px}
.add-cart{left:614px;top:425px;width:106px;height:24px;border-radius:12px;background:var(--navy);color:var(--white);font-size:8px;font-weight:700;line-height:24px;padding-left:38px}
.add-cart .dot{position:absolute;left:-1px;top:-3px;width:30px;height:30px;border-radius:50%;background:var(--pink);border:2px solid var(--white)}
.arrow{width:18px;height:18px;border-radius:50%;border:1px solid #999;background:linear-gradient(#fff,#ddd);color:#777;font-size:10px;text-align:center;line-height:16px}
.thumb{width:56px;height:55px;border:1px solid #ccc}

/* video */
.ribbon-title{left:74px;top:642px}
.ribbon-title span{position:absolute;left:40px;top:17px;color:var(--white);font-size:13.5px;white-space:nowrap}
.promo-text{left:115px;top:704px;width:205px;font-size:8px;line-height:12px}
.promo-btn{left:115px;top:754px;width:61px;height:23px;background:var(--navy);color:var(--white);font-size:8px;line-height:23px;text-align:center;border-radius:2px}
.video-panel{left:338px;top:632px;width:383px;height:242px}
.video{left:347px;top:642px;width:364px;height:190px;background:linear-gradient(90deg,#3e6a35 0%,#6b8f4f 45%,#c83030 60%,#d8392f 100%)}
.video-title{left:347px;top:779px;background:rgba(0,0,0,.55);color:var(--white);font-size:14px;padding:3px 6px}
.controls{left:347px;top:832px;width:364px;height:32px;background:linear-gradient(#f4f4f4,#d5d5d5)}
.play{left:359px;top:837px;width:34px;height:24px;background:#555;border-radius:2px}
.ctrl-arrow{width:24px;height:24px;border-radius:50%;background:#6d6d6d;color:#fff;font-size:11px;text-align:center;line-height:24px}
.pager i{position:absolute;top:0;width:5px;height:5px;border-radius:50%;border:1px solid #bbb;background:#fff}
.time{left:654px;top:844px;font-size:7.5px;color:#222}

/* banners */
.banner{top:906px;width:307px;height:118px;box-shadow:0 4px 6px rgba(0,0,0,.25)}
.banner-title{position:absolute;background:rgba(255,255,255,.7);color:#222;font-size:15px;font-weight:700;padding:2px 6px}

/* footer */
.footer{left:78px;top:1056px;width:656px;height:122px;background:var(--footer);color:var(--white);font-size:8px}
.col{position:absolute;top:40px;line-height:14.3px}
.footer-bar{left:78px;top:1178px;width:656px;height:22px;background:var(--footer-bar);color:var(--white);font-size:8px}
.social i{position:absolute;top:5px;width:12px;height:12px;border-radius:2px;background:#3a8af0}
</style>
</head>
<body>
<div class="page"></div>

<nav class="nav abs">
  <a class="home" href="#">Home</a>
  <a href="#" style="left:92px">Gallery</a>
  <a href="#" style="left:149px">Buy</a>
  <a href="#" style="left:194px">Contact</a>
  <div class="cart-link abs">
    <svg width="20" height="16" viewBox="0 0 20 16"><path d="M1 5h18l-2 9H3z" fill="none" stroke="#fff" stroke-width="1.6"/><path d="M6 5l4-4 4 4" fill="none" stroke="#fff" stroke-width="1.4"/></svg>
    0 item(s)-$0.00 &nbsp;&nbsp; view Cart(0)
  </div>
</nav>

<section class="hero photo" role="img" aria-label="Blue and red ride-on toy bikes on a leafy woodland path"></section>
<div class="logo abs"><span>Zippa<br>Roller</span></div>
<div class="caption cap1">Lorem ipsum dolor sit amet</div>
<div class="caption cap2">Consectetur adipisicing elit, sed</div>
<div class="caption cap3">Do eiusmod tempor</div>
<div class="hero-btn abs">Read more</div>
<div class="slider abs">
  <b style="left:9px">‹</b>
  <i style="left:53px"></i><i class="on" style="left:64px"></i><i style="left:75px"></i><i style="left:86px"></i><i style="left:97px"></i>
  <b style="left:135px">›</b>
</div>

<div class="product panel abs"></div>
<div class="product-photo photo" role="img" aria-label="Silver ride-on toy bike on a tree-lined road"></div>
<div class="price-tag abs">
  <svg width="254" height="48"><polygon points="8,0 254,0 254,48 8,48 0,24" fill="var(--pink-dark)"/><polygon points="14,4 250,4 250,42 14,42 6,23" fill="var(--pink)" stroke="#fff" stroke-width="1"/></svg>
  <div class="name abs">Zippa Roller</div>
  <div class="price abs">Price: <b>$50</b></div>
</div>
<div class="label abs" style="left:485px;top:427px">Color:</div>
<div class="swatch abs" style="left:526px;background:#d8262c"></div>
<div class="swatch abs" style="left:541px;background:#2aa6e0"></div>
<div class="swatch abs" style="left:556px;background:#e63e74"></div>
<div class="add-cart abs"><span class="dot"></span>ADD TO CART</div>
<div class="label abs" style="left:487px;top:482px">Gallery</div>
<div class="arrow abs" style="left:477px;top:543px">‹</div>
<div class="thumb photo" style="left:506px;top:524px;background:linear-gradient(#4d6b3b,#7a7a7a)" role="img" aria-label="Bike front wheel close-up"></div>
<div class="thumb photo" style="left:569px;top:524px;background:linear-gradient(#ddd,#777)" role="img" aria-label="Bike rear wheel close-up"></div>
<div class="thumb photo" style="left:631px;top:524px;background:linear-gradient(#3a3fd0,#20238a)" role="img" aria-label="Blue bike engine detail"></div>
<div class="arrow abs" style="left:697px;top:543px">›</div>

<div class="ribbon-title abs">
  <svg width="255" height="50"><polygon points="0,0 248,0 255,25 248,50 0,50" fill="var(--pink-dark)"/><polygon points="4,4 244,4 250,24 244,44 4,44" fill="var(--pink)" stroke="#fff" stroke-width="1"/></svg>
  <span>Promotional Videos</span>
</div>
<p class="promo-text abs">Lorem ipsum dolor sit amet, consectetur adipisicing elit, sed do eiusmod tempor incididunt ut labore et dolore magna aliqua.</p>
<div class="promo-btn abs">Read more</div>
<div class="arrow abs" style="left:95px;top:819px">‹</div>
<div class="thumb photo" style="left:124px;top:800px;background:linear-gradient(#3f6f35,#d33030)" role="img" aria-label="Video: red bike"></div>
<div class="thumb photo" style="left:187px;top:800px;background:linear-gradient(#2c4a2a,#3a8a3a)" role="img" aria-label="Video: red and blue bikes"></div>
<div class="thumb photo" style="left:251px;top:800px;background:linear-gradient(#5f9a44,#2aa6e0)" role="img" aria-label="Video: blue bike"></div>
<div class="arrow abs" style="left:315px;top:819px">›</div>

<div class="video-panel panel abs"></div>
<div class="video photo" role="img" aria-label="Animated movie still of a red bike on a mountain forest road"></div>
<svg class="abs" style="left:519px;top:727px" width="40" height="40"><circle cx="20" cy="20" r="19" fill="rgba(0,0,0,.35)"/><polygon points="14,10 31,20 14,30" fill="#fff"/></svg>
<div class="video-title abs">3D animate movie</div>
<div class="controls abs"></div>
<div class="play abs"><svg width="34" height="24"><polygon points="12,5 24,12 12,19" fill="#fff"/></svg></div>
<div class="ctrl-arrow abs" style="left:426px;top:836px">‹</div>
<div class="pager abs" style="left:486px;top:842px;width:60px;height:12px">
  <span class="abs" style="left:0;top:-2px;width:12px;height:12px;border-radius:50%;background:var(--label-blue);color:#fff;font-size:7px;text-align:center;line-height:12px">1</span>
  <i style="left:21px;top:3px"></i><i style="left:32px;top:3px"></i><i style="left:43px;top:3px"></i><i style="left:54px;top:3px"></i>
</div>
<div class="ctrl-arrow abs" style="left:590px;top:836px">›</div>
<div class="time abs">00:00 &nbsp; 05:56</div>

<div class="banner photo" style="left:91px;background:linear-gradient(#3c5a22,#6b8a3a 50%,#8a7a3a)" role="img" aria-label="Blue and red bikes on a forest track"><span class="banner-title" style="left:0;top:41px">Zippa Roller</span></div>
<div class="banner photo" style="left:413px;background:linear-gradient(#8fae5a,#9a9a9a 45%,#6f6f6f)" role="img" aria-label="Pink, blue and red bikes lined up on a road"><span class="banner-title" style="left:0;top:7px">Colors Of Bikes</span></div>

<footer class="footer abs">
  <svg class="abs" style="left:17px;top:30px" width="16" height="24" viewBox="0 0 16 24"><path d="M8 0a8 8 0 0 1 8 8c0 6-8 16-8 16S0 14 0 8a8 8 0 0 1 8-8z" fill="#fff"/><circle cx="8" cy="8" r="3" fill="var(--footer)"/></svg>
  <div class="col" style="left:44px;top:40px">CONTACT US AT:<br>12 Marrow Lane, Fenwick, 40218, Avalon<br>Phon: 1.800.555.0142 &amp; Fax: 1/800.555.0143<br>Email: <span style="color:#0b2a66">hello@zipparoller.example</span></div>
  <div class="col" style="left:232px">ABOUT US:<br>Our History<br>Our Clients<br>Partners<br>Meet the Team</div>
  <div class="col" style="left:341px">SERVICES:<br>General Practice<br>Business Law<br>Mediation<br>Civil Defense Law<br>Family Law</div>
  <div class="col" style="left:449px">CASE STUDIES:<br>Medical Malpraxis<br>DUI cases<br>Mediation cases<br>Family Law cases<br>Other studies</div>
  <div class="col" style="left:557px">CAREERS:<br>Available Jobs<br>Internship<br>Send your Resume</div>
</footer>
<div class="footer-bar abs">
  <span class="abs" style="left:43px;top:7px">Copyrights 2013 Zippa Roller</span>
  <div class="social">
    <i style="left:557px" aria-label="Social link"></i><i style="left:575px" aria-label="Social link"></i><i style="left:593px" aria-label="Social link"></i><i style="left:611px" aria-label="Social link"></i><i style="left:629px" aria-label="Social link"></i>
  </div>
</div>
</body>
</html>
```